Retail Jewelry Business Card Design Project

We are in need of a new business card design for a retail jewelry store. This store is in the business of fine jewelry including but not specific to bridal jewelry, diamonds, designer jewelry and watches.

This store has been in business for 20 years but continues to strive for a modern professional appeal. The main colors use for this business are a royal blue, white and silver.

Target Market(s)

Target market is ages 18-50

Industry/Entity Type

Jewelry

Requirements
Must have
• Sales Person Name
Sales Person Email Address

Store Address
Store Phone
Website

Standard business card size. No odd shapes or sizes.
Nice to have
• Overall modern feel for card.

We have thought that a design with a nice feature of the logo on the back of the card would be nice but open to ideas.
Should not have
• No specific images of jewelry should be used.

```html
<!DOCTYPE html>
<html lang="en">
<head>
<meta charset="utf-8">
<title>Marlowe Lane Fine Jewelry – Business Card</title>
<link href="https://fonts.googleapis.com/css2?family=Jost:wght@400;700&display=swap" rel="stylesheet">
<style>
  :root {
    --card-bg: #ffffff;
    --card-border: #000000;
    --silver-text: #b3c0cb;
    --royal-blue: #0a14e6;
  }
  html, body {
    margin: 0;
    padding: 0;
    width: 1200px;
    height: 698px;
    overflow: hidden;
    background: var(--card-bg);
  }
  .card {
    position: relative;
    width: 1200px;
    height: 698px;
    box-sizing: border-box;
    border: 4px solid var(--card-border);
    background: var(--card-bg);
    font-family: "Jost", "Futura", sans-serif;
    color: var(--silver-text);
  }
  .brand {
    position: absolute;
    top: 54px;
    left: 700px;
    width: 440px;
    text-align: center;
    color: var(--royal-blue);
    font-weight: 400;
    line-height: 1;
  }
  .brand-name {
    display: block;
    font-size: 72px;
    letter-spacing: 1px;
    white-space: nowrap;
  }
  .brand-tagline {
    display: block;
    margin-top: 22px;
    font-size: 26px;
    letter-spacing: 5px;
    text-transform: uppercase;
  }
  .contact-person {
    position: absolute;
    left: 88px;
    top: 182px;
    line-height: 1;
  }
  .person-name {
    margin: 0;
    font-size: 41px;
    font-weight: 700;
    letter-spacing: 0.5px;
    text-transform: uppercase;
    white-space: nowrap;
  }
  .person-email {
    display: block;
    margin-top: 10px;
    font-size: 37px;
    font-weight: 400;
  }
  .store-details {
    position: absolute;
    left: 88px;
    top: 378px;
    margin: 0;
    font-style: normal;
    font-size: 37px;
    font-weight: 400;
    line-height: 49px;
  }
  .store-details span { display: block; white-space: nowrap; }
</style>
</head>
<body>
  <main class="card">
    <div class="brand">
      <span class="brand-name">Marlowe Lane</span>
      <span class="brand-tagline">Fine Jewelry</span>
    </div>

    <section class="contact-person">
      <h1 class="person-name">Evan Marlowe Hadley</h1>
      <span class="person-email">evan@marlowelanejewelry.com</span>
    </section>

    <address class="store-details">
      <span class="store-name">Marlowe Lane Fine</span>
      <span class="store-street">2280 Bayfront Street</span>
      <span class="store-city">Harbor Point, FL 32099</span>
      <span class="store-phone">(850) 555-0148</span>
      <span class="store-web">www.marlowelanejewelry.com</span>
    </address>
  </main>
</body>
</html>
```